Tildens Biscuit Barn Website

I need a website for a diner/restaurant that has been established in a farming, oil and industrial community for over 15 years. The website needs to be simple in design, but that should demonstrate the mastery of skills of the designer. Our diner/restaurant is family oriented, patriotic but very rustic
Fb Address is fb.me/TildensBarn

Pictures of the restaurant

https://www.filecrate-example.net/s/qk72hdw01/Tildens_05.jpg

Pictures of About us

https://www.filecrate-example.net/sh/zm40vrt88/AboutUsPhotos

Article about Tilden's
https://www.filecrate-example.net/s/wp31nbx57/TildensBiscuitBarn1.PDF
https://www.filecrate-example.net/s/hy65lcu29/TildensBiscuitBarn2.PDF

Reason: I was slow to update with information.

Reason: I am just getting feedback to the designs posted. I wasn't sure of the limited feedback was limiting designers from submitting designs. That and running a business with 25 employees open 12 hours a day, being here 2 hours prior and 2-3 hours after makes for long days.

I've increased the first place prize and also added funds to the second and third place prizes for your effort.

I just need the files in PSD, not HTML 5 as originally requested. We can handle getting the coding part.

Ill have the contest finalized by Monday. Thanks for your patience.

Target Market(s)

Cross section of adults from 18-35 & 35-55.

Industry/Entity Type

Industrial

Font styles to use
Other font styles liked:
• ff tisa web pro or garamond premier pro

Requirements
Must have
• Must be clean, look nice and not look like an afterthought.
Nice to have
• Please see the last two documents for information about our restaurant, which was featured in our local newspaper.

```html
<!DOCTYPE html>
<html lang="en">
<head>
<meta charset="utf-8">
<title>Tilden's Biscuit Barn</title>
<link rel="stylesheet" href="https://fonts.googleapis.com/css2?family=Fira+Sans:ital,wght@0,400;0,500;0,700;1,500;1,700&family=Open+Sans:wght@400;600&family=Lobster&display=swap">
<style>
  :root {
    --page-dark: #2b2b2b;
    --page-mid: #4a4a4a;
    --footer-brown: #231a0e;
    --nav-teal: #1d5d78;
    --info-grey: #3b3b3b;
    --logo-black: #050505;
    --accent-pink: #b0184a;
    --accent-teal: #1f5f78;
    --panel-dark: #151515;
    --panel-first: #1c1c1c;
    --gold: #f0b43a;
    --button-gold: #f5c766;
    --text-light: #ffffff;
    --text-soft: #cfcfcf;
    --text-muted: #8a8a8a;
    --footer-text: #d8d0c2;
    --footer-rule: #4a3e2d;
    --heading-teal: #3d93b5;
  }
  * { margin: 0; padding: 0; box-sizing: border-box; }
  html, body { width: 1075px; height: 1200px; overflow: hidden; }
  body {
    position: relative;
    font-family: "Open Sans", sans-serif;
    background: var(--footer-brown);
    color: var(--text-light);
  }
  .backdrop {
    position: absolute; left: 0; top: 0; width: 1075px; height: 836px;
    background: radial-gradient(ellipse at 50% 60%, #6a6a6a 0%, var(--page-mid) 35%, var(--page-dark) 80%);
  }
  .site-header { position: absolute; left: 125px; top: 0; width: 825px; height: 152px; }
  .brand {
    position: absolute; left: 0; top: 0; width: 260px; height: 152px;
    background: var(--logo-black);
    display: flex; align-items: center; justify-content: center; gap: 10px;
  }
  .brand-dot { width: 14px; height: 14px; border-radius: 50%; background: var(--accent-pink); }
  .brand-name { font-family: "Fira Sans", sans-serif; font-weight: 700; font-size: 30px; color: var(--accent-pink); }
  .main-nav {
    position: absolute; left: 260px; top: 0; width: 565px; height: 48px;
    background: var(--nav-teal);
    display: flex; align-items: center; justify-content: space-around; padding: 0 12px;
    font-family: "Fira Sans", sans-serif; font-size: 16px;
  }
  .main-nav a { color: #b9d3de; text-decoration: none; }
  .main-nav a.is-current { color: var(--text-light); font-weight: 500; }
  .info-bar {
    position: absolute; left: 260px; top: 48px; width: 565px; height: 104px;
    background: var(--info-grey); display: flex;
    font-family: "Fira Sans", sans-serif;
  }
  .info-block { padding: 22px 0 0 43px; }
  .info-block + .info-block { border-left: 1px solid #555; }
  .info-block.join { width: 165px; }
  .info-block.menu { width: 170px; }
  .info-title { font-size: 13px; letter-spacing: .2px; margin-bottom: 10px; }
  .social { display: flex; gap: 7px; }
  .social span { width: 20px; height: 20px; border-radius: 3px; background: #8a8a8a; }
  .social span:first-child { background: #b8862a; }
  .menu-link, .location { display: flex; align-items: center; gap: 8px; font-size: 12px; font-weight: 500; }
  .location { align-items: flex-start; line-height: 15px; gap: 10px; font-size: 11.5px; }
  .info-block.find { padding-left: 43px; }
  .hero {
    position: absolute; left: 125px; top: 152px; width: 825px; height: 375px;
    background: radial-gradient(ellipse at 55% 50%, #d9a44a 0%, #b9752c 30%, #8a3a1c 60%, #3a1a10 100%);
  }
  .hero-caption {
    position: absolute; left: 0; padding: 0 17px; height: 36px; line-height: 36px;
    font-family: "Fira Sans", sans-serif; font-size: 21px; color: var(--text-light);
  }
  .hero-caption.first { top: 224px; width: 264px; background: var(--accent-pink); }
  .hero-caption.second { top: 261px; width: 293px; background: var(--accent-teal); }
  .features {
    position: absolute; left: 125px; top: 556px; width: 825px; height: 249px;
    background: var(--panel-dark); border-top: 10px solid #2a2a2a;
    display: flex; box-shadow: 0 4px 12px rgba(0,0,0,.5);
  }
  .feature { width: 206.25px; position: relative; }
  .feature.is-active { background: var(--panel-first); }
  .feature.is-active::before {
    content: ""; position: absolute; left: 0; top: -10px; width: 100%; height: 10px; background: var(--accent-pink);
  }
  .feature-photo { height: 100px; }
  .feature:not(.is-active) .feature-photo { opacity: .45; }
  .feature-title { font-family: "Fira Sans", sans-serif; font-size: 14px; margin: 16px 0 12px 21px; color: var(--text-soft); }
  .feature.is-active .feature-title { color: var(--heading-teal); }
  .feature-text { font-size: 10.5px; line-height: 17px; color: var(--text-muted); margin: 0 20px 0 21px; }
  .footer-col { position: absolute; top: 852px; }
  .footer-col h3 {
    font-family: "Fira Sans", sans-serif; font-weight: 500; font-size: 16px; color: var(--gold);
    padding-bottom: 12px; border-bottom: 1px solid var(--footer-rule); margin-bottom: 18px;
  }
  .footer-col p, .footer-col li { font-size: 10px; line-height: 17px; color: var(--footer-text); }
  .balance { left: 125px; width: 180px; }
  .balance p { margin-bottom: 25px; }
  .menu-col { left: 356px; width: 192px; }
  .news-col { left: 600px; width: 158px; }
  .resources { left: 811px; width: 140px; }
  .resources ul { list-style: none; }
  .resources li { margin-bottom: 8px; }
  .dish { display: flex; gap: 8px; padding-bottom: 10px; border-bottom: 1px solid var(--footer-rule); margin-bottom: 10px; }
  .dish-photo { width: 60px; height: 60px; border-radius: 50%; flex: none;
    background: radial-gradient(circle at 60% 45%, #e7e3dd 0%, #b9b2a8 45%, #6a4c2e 100%); }
  .dish-name { font-family: "Fira Sans", sans-serif; font-style: italic; font-weight: 500; font-size: 11px; color: var(--gold); }
  .news-item { padding-bottom: 10px; border-bottom: 1px solid var(--footer-rule); margin-bottom: 12px; }
  .news-meta { display: flex; justify-content: space-between; font-size: 10px; margin-top: 2px; }
  .news-date { font-style: italic; color: var(--gold); padding-left: 3px; }
  .news-more { color: var(--text-light); font-weight: 600; }
  .button {
    position: absolute; top: 1061px; height: 24px; padding: 0 8px; line-height: 24px;
    background: var(--button-gold); border-radius: 2px;
    font-family: "Fira Sans", sans-serif; font-style: italic; font-weight: 700; font-size: 11.5px; color: #2a1d0c;
  }
  .site-footer {
    position: absolute; left: 125px; top: 1140px; width: 825px; border-top: 1px solid var(--footer-rule);
    display: flex; justify-content: space-between; padding-top: 22px; font-size: 10.5px; color: #7e7565;
  }
  .legal a { color: #7e7565; text-decoration: none; }
  .legal a.is-strong { color: var(--text-light); }
</style>
</head>
<body>
  <div class="backdrop" role="img" aria-label="Blurred black and white photo of diner guests"></div>

  <header class="site-header">
    <div class="brand"><span class="brand-dot"></span><span class="brand-name">Tilden's</span></div>
    <nav class="main-nav">
      <a href="#" class="is-current">Home</a><a href="#">Our History</a><a href="#">Menu</a><a href="#">Events</a><a href="#">News</a><a href="#">Contact Us</a>
    </nav>
    <div class="info-bar">
      <div class="info-block join">
        <div class="info-title">JOIN US</div>
        <div class="social"><span></span><span></span><span></span></div>
      </div>
      <div class="info-block menu">
        <div class="info-title">VIEW MENU</div>
        <div class="menu-link">
          <svg width="38" height="22" viewBox="0 0 38 22"><path d="M4 6 L30 2 L36 14 L10 20 Z" fill="#4fa7c9"/><path d="M16 7 L22 15 M22 7 L16 15" stroke="#fff" stroke-width="2"/></svg>
          Pizza
        </div>
      </div>
      <div class="info-block find">
        <div class="info-title">FIND A LOCATION</div>
        <div class="location">
          <svg width="18" height="28" viewBox="0 0 18 28"><path d="M9 1 C4 1 1 5 1 9 C1 15 9 24 9 24 C9 24 17 15 17 9 C17 5 14 1 9 1 Z" fill="#2a86b0"/><circle cx="9" cy="9" r="3.2" fill="#3b3b3b"/><ellipse cx="9" cy="26" rx="5" ry="1.5" fill="#2a86b0"/></svg>
          <span>4820 Ridgeline Hwy<br>Fairmont, California</span>
        </div>
      </div>
    </div>
  </header>

  <section class="hero" role="img" aria-label="Platter of nachos, egg rolls, salsa and guacamole">
    <div class="hero-caption first">Lorem ipsum dolor sit</div>
    <div class="hero-caption second">consectetur lorem ispum</div>
  </section>

  <section class="features">
    <article class="feature is-active">
      <div class="feature-photo" role="img" aria-label="Two guests seated at a diner table" style="background:linear-gradient(135deg,#c9d3dd,#6d7580 55%,#2d2f33)"></div>
      <h2 class="feature-title">Welcome to Tilden's</h2>
      <p class="feature-text">Lorem ipsum dolor sit amet tetur a adipiscing elit. Pellentese eget ipsum ac ex dignissim convallis ac id felis pelltesque eget.</p>
    </article>
    <article class="feature">
      <div class="feature-photo" role="img" aria-label="Condiments and cups on a diner counter" style="background:linear-gradient(135deg,#8b8f96,#4a6f9a 50%,#5a3a2a)"></div>
      <h2 class="feature-title">Our Special Coffee</h2>
      <p class="feature-text">Lorem ipsum dolor sit amet tetur a adipiscing elit. Pellentese eget ipsum ac ex dignissim convallis ac id felis pelltesque eget.</p>
    </article>
    <article class="feature">
      <div class="feature-photo" role="img" aria-label="Busy diner dining room" style="background:linear-gradient(135deg,#6b86a8,#a2815e 50%,#4a3528)"></div>
      <h2 class="feature-title">Our Menu</h2>
      <p class="feature-text">Lorem ipsum dolor sit amet tetur a adipiscing elit. Pellentese eget ipsum ac ex dignissim convallis ac id felis pelltesque eget.</p>
    </article>
    <article class="feature">
      <div class="feature-photo" role="img" aria-label="Guests in costume at a diner event" style="background:linear-gradient(135deg,#8c7a6a,#c8c2c0 45%,#6a2a2a)"></div>
      <h2 class="feature-title">Best News Sign Up</h2>
      <p class="feature-text">Lorem ipsum dolor sit amet tetur a adipiscing elit. Pellentese eget ipsum ac ex dignissim convallis ac id felis pelltesque eget.</p>
    </article>
  </section>

  <section class="footer-col balance">
    <h3>Check Your Balance</h3>
    <p>Find out how much Harlow's goodness you have left on your card. You're just a click away!</p>
    <p>Find out how much Harlow's good-ness you have left on your card. You're just a click away!</p>
  </section>
  <section class="footer-col menu-col">
    <h3>View Menu</h3>
    <div class="dish"><div class="dish-photo" role="img" aria-label="Coffee cup seen from above"></div><div><div class="dish-name">Lorem ispum</div><p>Lorem ipsum dolor sit amet, consectetur adipisc-</p></div></div>
    <div class="dish"><div class="dish-photo" role="img" aria-label="Coffee cup seen from above"></div><div><div class="dish-name">Lorem ispum</div><p>Lorem ipsum dolor sit amet, consectetur adipisc-</p></div></div>
  </section>
  <section class="footer-col news-col">
    <h3>Latest News</h3>
    <div class="news-item"><p>Harlow's Selected Among Top 50 Franchises for Veterans</p><div class="news-meta"><span class="news-date">7/27/2013</span><span class="news-more">Read more</span></div></div>
    <div class="news-item"><p>Harlow's Selected Among Top 50 Franchises for Veterans</p><div class="news-meta"><span class="news-date">7/27/2013</span><span class="news-more">Read more</span></div></div>
  </section>
  <section class="footer-col resources">
    <h3>Resources</h3>
    <ul><li>Download a Menu</li><li>Employment Opportunities</li><li>Join the E-Club</li><li>Harlow's New Book</li><li>Our Official Photo Gallery</li></ul>
  </section>

  <a class="button" style="left:125px">Click Hear</a>
  <a class="button" style="left:356px">See our menu</a>
  <a class="button" style="left:602px">Read more</a>

  <footer class="site-footer">
    <span>© 2013 Tildens Biscuit Barn. All rights reserved.</span>
    <span class="legal"><a href="#" class="is-strong">Terms of Use</a> &nbsp;/&nbsp; <a href="#">Privacy Policy</a> &nbsp;/&nbsp; <a href="#">Site map</a></span>
  </footer>
</body>
</html>
```